Re-design of Business Card

We require a design for our business card.

Korrim is a supplier of industrial packaging specializing in plastic products. We are undergoing a rebranding to appear more corporate. We have changed our company name to korrim and have a new logo.

I have uploaded our old card design with the previous company name.
Don't copy the current design. We are looking for a new design.

Industry/Entity Type

Manufacturing

Contact Information for Business Card

please don't copy the current design. we are looking for a new design.

Font styles to use
Sans Serif

Colors

Designer to choose colors to be used in the design.

Requirements
Must have
• clean and easy to read.

```html
<!DOCTYPE html>
<html lang="en">
<head>
<meta charset="UTF-8">
<title>Korrim Business Card</title>
<link href="https://fonts.googleapis.com/css2?family=Lato:wght@400;700;900&display=swap" rel="stylesheet">
<style>
  :root {
    --brand-orange: #f47f20;
    --card-white: #ffffff;
    --text-dark: #333333;
    --text-mid: #555555;
    --backdrop: #d6d6d6;
    --shadow: rgba(0, 0, 0, 0.18);
  }
  * { margin: 0; padding: 0; box-sizing: border-box; }
  html, body {
    width: 1200px;
    height: 900px;
    overflow: hidden;
  }
  body {
    background: var(--backdrop);
    font-family: "Lato", sans-serif;
    position: relative;
  }
  .card {
    position: absolute;
    width: 540px;
    height: 310px;
    border-radius: 26px;
    box-shadow: 0 10px 24px var(--shadow);
    overflow: hidden;
  }
  .card-back {
    left: 80px;
    top: 120px;
    background: var(--brand-orange);
    display: flex;
    align-items: center;
    justify-content: center;
  }
  .card-back .wordmark {
    color: var(--card-white);
    font-weight: 900;
    font-size: 58px;
    letter-spacing: 2px;
  }
  .card-front {
    left: 580px;
    top: 470px;
    background: var(--card-white);
  }
  .front-wordmark {
    position: absolute;
    left: 36px;
    top: 58px;
    display: flex;
    align-items: center;
    gap: 12px;
    color: var(--brand-orange);
    font-weight: 900;
    font-size: 50px;
    letter-spacing: 2px;
  }
  .front-wordmark .mark-square {
    width: 22px;
    height: 22px;
    background: var(--brand-orange);
  }
  .person {
    position: absolute;
    left: 36px;
    top: 138px;
  }
  .person-name {
    color: var(--brand-orange);
    font-weight: 700;
    font-size: 19px;
    letter-spacing: 0.5px;
    text-transform: uppercase;
  }
  .person-role {
    color: var(--text-dark);
    font-size: 15px;
    margin-top: 1px;
  }
  .contact-list {
    position: absolute;
    left: 36px;
    top: 196px;
    list-style: none;
  }
  .contact-list li {
    display: flex;
    align-items: center;
    gap: 10px;
    color: var(--text-dark);
    font-size: 14.5px;
    line-height: 19px;
  }
  .contact-list svg {
    width: 12px;
    height: 12px;
    fill: var(--brand-orange);
    flex: none;
  }
  .head-office {
    position: absolute;
    right: 34px;
    top: 60px;
    text-align: right;
  }
  .head-office-label {
    color: var(--brand-orange);
    font-size: 15px;
    letter-spacing: 0.5px;
    text-transform: uppercase;
  }
  .head-office-address {
    color: var(--text-dark);
    font-size: 14px;
    line-height: 18px;
    margin-top: 2px;
  }
</style>
</head>
<body>

  <div class="card card-back">
    <span class="wordmark">KORRIM</span>
  </div>

  <div class="card card-front">
    <div class="front-wordmark">
      <span class="mark-square"></span>
      <span>KORRIM</span>
    </div>

    <div class="person">
      <div class="person-name">Dana Whitlock</div>
      <div class="person-role">Machinery Sales Manager</div>
    </div>

    <ul class="contact-list">
      <li>
        <svg viewBox="0 0 12 12" aria-hidden="true"><path d="M2 1h2.5l1 2.5-1.5 1a6 6 0 0 0 3.5 3.5l1-1.5 2.5 1V11c-5.5 0-9-3.5-9-9z"/></svg>
        1300 468 210
      </li>
      <li>
        <svg viewBox="0 0 12 12" aria-hidden="true"><path d="M3 0h6v12H3z M4 1.5v8h4v-8z"/></svg>
        XXXX XXX XXX
      </li>
      <li>
        <svg viewBox="0 0 12 12" aria-hidden="true"><path d="M3 0h6v4H3z M1 4.5h10V10H9v2H3v-2H1z M4 8v3h4V8z"/></svg>
        +61 7 3580 4127
      </li>
      <li>
        <svg viewBox="0 0 12 12" aria-hidden="true"><path d="M0 2h12v8H0z M1 3l5 3.5L11 3z" fill-rule="evenodd"/></svg>
        dana@korrim.com.au
      </li>
      <li>
        <svg viewBox="0 0 12 12" aria-hidden="true"><circle cx="6" cy="6" r="6"/></svg>
        www.halvernpack.com.au
      </li>
    </ul>

    <div class="head-office">
      <div class="head-office-label">Head Office</div>
      <div class="head-office-address">48 Harlow St Northgate<br>Park, Qld 4210 Australia</div>
    </div>
  </div>

</body>
</html>
```